IT Freelancer (Consulting, trainer and project manager) needed letterhead

As a freelancer for IT Trainingswhip, consulting and project management I need a letterhead design. What is desired is a design that fits the existing logo (see Annex). It is functional, reliable, and equal time wirkenn Agil and modern. The whole is in color, as well as printed out to make a good impression on a black and white printer. The whole is to the existing Cooperate design (business card, homepage, logo) fit. Therefore, the choice of colors.
Updates

Target Market(s)

Customers such as medium-sized enterprises, training institutions

Industry/Entity Type

Consulting

Colors
0455a3
3277b5
85abd2
cfdfed
34a6d7
32a6d6
249fd4
0792cd
85cae6

Requirements
Must have
• Must include logo (see Annex) address (Brennerweg 14, 95652 Waldsassen, Germany). Must seriously and act simultaneously Agil. Design should (even) be adaptable (signature, address, etc.) design must look good on a black / white laser

```html
<!DOCTYPE html>
<html lang="de">
<head>
<meta charset="utf-8">
<title>Lorenz Hafner – Briefbogen</title>
<link href="https://fonts.googleapis.com/css2?family=Lato:wght@400;700;900&display=swap" rel="stylesheet">
<style>
  :root {
    --blue-dark: #0455a3;
    --blue-mid: #3277b5;
    --blue-light: #34a6d7;
    --ink: #1e1e1e;
    --muted: #444;
    --paper: #ffffff;
    --backdrop: #ececec;
  }
  * { margin: 0; padding: 0; box-sizing: border-box; }
  html, body {
    width: 1200px; height: 794px; overflow: hidden;
    background: var(--backdrop);
    font-family: "Lato", sans-serif;
    color: var(--ink);
  }
  .letterhead {
    position: absolute;
    left: 331px; top: 17px;
    width: 537px; height: 760px;
    background: var(--paper);
    box-shadow: 0 2px 10px rgba(0,0,0,.12);
    overflow: hidden;
  }
  .top-rule {
    position: absolute; left: 0; top: 0; width: 100%; height: 3px;
    background: var(--blue-dark);
  }
  .brand {
    position: absolute; right: 40px; top: 34px;
    display: flex; align-items: center; gap: 8px;
  }
  .brand-dot {
    width: 34px; height: 34px; border-radius: 50%;
    background: var(--blue-dark);
  }
  .brand-name {
    font-weight: 900; font-size: 15px; letter-spacing: .5px;
    color: var(--blue-dark); text-transform: uppercase; line-height: 1;
  }
  .contact {
    position: absolute; right: 40px; top: 82px;
    text-align: right; font-size: 6.5px; line-height: 9px; color: var(--muted);
    font-style: normal;
  }
  .contact .row { display: flex; justify-content: flex-end; align-items: center; gap: 4px; }
  .contact svg { width: 6px; height: 6px; fill: var(--blue-dark); }
  .sender-line {
    position: absolute; left: 58px; top: 186px;
    font-size: 5.5px; color: var(--muted);
  }
  .body-copy {
    position: absolute; left: 58px; top: 300px; width: 410px;
    font-size: 8.6px; line-height: 11.2px;
  }
  .body-copy p { margin-bottom: 11px; }
  .footer-band { position: absolute; left: 0; bottom: 0; width: 100%; height: 60px; }
  .web {
    position: absolute; right: 22px; bottom: 28px;
    font-size: 9px; color: #fff; letter-spacing: .2px;
  }
</style>
</head>
<body>
  <main class="letterhead">
    <div class="top-rule"></div>

    <header class="brand">
      <span class="brand-dot"></span>
      <span class="brand-name">Lorenz Hafner</span>
    </header>

    <address class="contact">
      <div class="row">Brennerweg 14</div>
      <div class="row">95699 Tannried</div>
      <div class="row">Deutschland</div>
      <div class="row">512 004 7300
        <svg viewBox="0 0 10 10"><path d="M2 1l2 0 1 2.5-1.2 1a5 5 0 0 0 2.7 2.7l1-1.2L10 7v2a1 1 0 0 1-1 1A8 8 0 0 1 1 2a1 1 0 0 1 1-1z"/></svg></div>
      <div class="row">512 004 7301
        <svg viewBox="0 0 10 10"><rect x="1" y="4" width="8" height="5"/><rect x="3" y="1" width="4" height="3"/></svg></div>
      <div class="row">info@lorenzhafner.de
        <svg viewBox="0 0 10 10"><rect x="0.5" y="2" width="9" height="6" rx="1"/></svg></div>
    </address>

    <div class="sender-line">Lorenz Hafner · Brennerweg 14 · 95699 Tannried · Deutschland</div>

    <section class="body-copy">
      <p>Lorem ipsum dolor sit amet, consectetur adipiscing elit. Praesent non est diam. Vivamus risus sem, gravida sit amet nibh ut, ornare lobortis ante. Aliquam sollicitudin, mauris tincidunt semper venenatis, orci est pretium augue, ut vestibulum felis velit bibendum urna. Integer sollicitudin aliquet ligula, non ultricies nisl efficitur nec. Aliquam felis lorem, facilisis ac condimentum quis, consectetur volutpat lacus. Proin fermentum sem quis elit efficitur, eu tempus magna maximus.</p>
      <p>Aenean a mi tortor. Morbi pretium mi sed cursus vehicula. Lorem ipsum dolor sit amet, consectetur adipiscing elit. In finibus eros ac maximus finibus. Nunc pretium pellentesque tellus. Nullam accumsan nisl non diam commodo sagittis. Nunc et ante sit amet urna auctor convallis. Maecenas sed fringilla metus, sit amet vulputate felis. Morbi eget tempor nisi. Aliquam erat volutpat. Aenean laoreet interdum tempus.</p>
      <p>Maecenas dignissim placerat mauris, vitae sollicitudin ex. Integer bibendum maximus mauris, ac tempor urna viverra id. Integer tincidunt lobortis nisl at posuere. Sed faucibus vulputate finibus. Maecenas convallis, sem quis pellentesque cursus, urna quam aliquam augue, quis porttitor eros est nec lectus. Sed mattis at tellus ut blandit. Aenean nunc magna, viverra sed mauris vel, porta finibus lacus. Nullam bibendum turpis rutrum porta placerat.</p>
      <p>Aenean a mi tortor. Morbi pretium mi sed cursus vehicula. Lorem ipsum dolor sit amet, consectetur adipiscing elit. In finibus eros ac maximus finibus. Nunc pretium pellentesque tellus. Nullam accumsan nisl non diam commodo sagittis. Nunc et ante sit amet urna auctor convallis. Maecenas sed fringilla metus, sit amet vulputate felis. Morbi eget tempor nisi. Aliquam erat volutpat. Aenean laoreet interdum tempus..</p>
    </section>

    <svg class="footer-band" viewBox="0 0 537 60" preserveAspectRatio="none" aria-hidden="true">
      <rect x="0" y="45" width="537" height="15" fill="var(--blue-light)"/>
      <path d="M300 60 L300 40 Q300 18 322 18 L537 18 L537 60 Z" fill="var(--blue-dark)"/>
    </svg>
    <div class="web">www.lorenzhafner.de</div>
  </main>
</body>
</html>
```